依頼詳細
ラフ案を添付致しますのでそちらをベースにブラッシュアップお願いいたします。

お水の特徴は以下となります。
①分子が細かい(水分子のナノコロイダル化、六角形構造)
②浸透力が高い(脳細胞まで届くイメージ)
③科学的に研究された機能のある水

全体デザインは、上記イメージを踏まえてエネルギー溢れるようなデザインを希望致します。
記載項目
下部に記載する社名等はデザイン選定後にお伝えさせていただきます。
サイズ
A4
ページ数
片面
希望イメージ
シンプル 複雑
単色 カラフル
暗い 明るい
日常 高級
遊び心 厳粛
未来的 伝統的
女性的 男性的
希望する色
水色系
納品ファイル
• 高解像度JPG (.jpg)
• イラストレーター形式 (.ai)
• PNG形式 (.png)
補足説明
■ 選んだ理由

インパクトと躍動感のあるデザインだった為選ばせて頂きました。

■ 提案者全員のお礼・コメント

この度はたくさんのご提案誠にありがとうございます。
素敵なデザインが多く選定に悩ませて頂きました。
また機会がありましたらその際はどうぞよろしくお願い致します。

```html
<!DOCTYPE html>
<html lang="ja">
<head>
<meta charset="UTF-8">
<title>高濃度シリカ水</title>
<link href="https://fonts.googleapis.com/css2?family=Noto+Sans+JP:wght@400;500;700;900&family=Playfair+Display:ital,wght@1,700&display=swap" rel="stylesheet">
<style>
:root{
  --blue:#1f63b4;
  --blue-deep:#0f3f86;
  --sky:#3aa7dd;
  --sky-pale:#dff1fb;
  --orange:#e8641d;
  --ink:#1f2a3a;
  --white:#ffffff;
}
*{margin:0;padding:0;box-sizing:border-box}
html,body{width:846px;height:1200px;overflow:hidden;background:var(--white)}
body{font-family:"Noto Sans JP",sans-serif;color:var(--ink)}
.flyer{position:relative;width:846px;height:1200px;overflow:hidden;background:var(--white)}
.footer-fade{position:absolute;left:0;bottom:0;width:846px;height:160px;background:linear-gradient(180deg,#ffffff,var(--sky-pale));z-index:0}
.visual{position:absolute;left:0;top:200px;width:846px;height:420px;z-index:0;
  background:radial-gradient(ellipse at 30% 55%,rgba(255,200,60,.55),transparent 45%),
  radial-gradient(ellipse at 70% 45%,rgba(60,170,230,.6),transparent 50%),
  radial-gradient(ellipse at 50% 70%,rgba(230,80,140,.45),transparent 50%),
  linear-gradient(180deg,#ffffff 0%,#eaf6fc 60%,#ffffff 100%)}
.title{position:absolute;left:30px;top:34px;font-size:72px;font-weight:900;letter-spacing:2px;color:var(--blue);line-height:1.2;white-space:nowrap;z-index:2}
.lot-badge{position:absolute;left:632px;top:12px;width:156px;height:156px;border-radius:50%;background:var(--sky);color:var(--white);text-align:center;font-weight:900;padding-top:32px;z-index:2}
.lot-badge .small{font-size:25px;display:block}
.lot-badge .big{font-size:40px;display:block;line-height:1.15}
.lot-badge .big span{font-size:21px}
.catch{position:absolute;left:115px;top:168px;font-size:27px;font-weight:700;color:var(--orange);letter-spacing:1px;z-index:2}
.point{position:absolute;border-radius:50%;display:flex;flex-direction:column;align-items:center;justify-content:center;text-align:center;font-weight:700;line-height:1.35;z-index:2}
.point.fill{background:var(--sky);color:var(--white);font-size:26px;box-shadow:0 4px 12px rgba(20,80,140,.25)}
.point.plain{background:var(--white);color:var(--blue-deep);font-size:24px;box-shadow:0 4px 12px rgba(20,80,140,.2)}
.point.plain small{font-size:15px;font-weight:500;margin-top:4px}
.p1{left:60px;top:200px;width:160px;height:160px}
.p2{left:50px;top:365px;width:170px;height:170px}
.p3{left:680px;top:240px;width:152px;height:152px}
.p4{left:660px;top:390px;width:170px;height:170px}
.about{position:absolute;left:0;top:585px;width:846px;height:190px;background:linear-gradient(180deg,var(--sky-pale),#ffffff);z-index:1}
.about h2{font-family:"Playfair Display",serif;font-style:italic;font-size:50px;color:var(--blue);text-align:center;margin-top:8px}
.about p{font-size:21px;font-weight:700;color:var(--ink);text-align:center;line-height:1.6;margin-top:8px}
.about p em{font-style:normal;color:var(--orange)}
.col-left{position:absolute;left:40px;top:780px;width:340px;z-index:2}
.col-left h3,.col-right h3{font-size:34px;font-weight:900;color:var(--blue);line-height:1.3}
.col-left ul{list-style:none;margin-top:18px;font-size:17px;line-height:1.6;color:var(--ink)}
.col-left li::before{content:"●";color:var(--sky);margin-right:4px}
.times{position:absolute;left:395px;top:800px;font-size:70px;font-weight:400;color:var(--blue-deep);z-index:2}
.col-right{position:absolute;left:500px;top:780px;width:320px;z-index:2}
.compare{display:flex;gap:14px;margin-top:18px}
.compare figure{flex:1}
.compare .swatch{height:84px;border-radius:6px}
.compare .normal{background:linear-gradient(135deg,#b9d7ee,#6fa6d6)}
.compare .active{background:linear-gradient(135deg,#cfeefd,#54b5e6)}
.compare figcaption{font-size:14px;text-align:center;margin-top:4px}
.col-right p{font-size:19px;font-weight:700;color:var(--blue-deep);margin-top:10px;line-height:1.5}
</style>
</head>
<body>
<main class="flyer">
  <div class="footer-fade"></div>
  <div class="visual" role="img" aria-label="カラフルな水しぶきを背景にしたシリカ水のペットボトル2本の写真"></div>
  <h1 class="title">高濃度シリカ水</h1>
  <div class="lot-badge"><span class="small">小ロット</span><span class="big">100<span>本～</span></span></div>
  <p class="catch">話題のシリカ水を自社ブランドでつくりませんか?</p>

  <div class="point fill p1">シリカ濃度<br>調整可</div>
  <div class="point plain p2">非晶質シリカ<small>「水溶性ケイ素miro」<br>配合</small></div>
  <div class="point fill p3">選べる<br>サイズ</div>
  <div class="point fill p4">科学的に<br>優れた<br>機能水</div>

  <section class="about">
    <h2>What is Silica?</h2>
    <p>注目のミネラル<em>「シリカ」</em>とカラダに浸透しやすい機能水をブレンドし<br>独自技術によってナノコロイダル化に成功した高濃度シリカ水</p>
  </section>

  <section class="col-left">
    <h3>非晶質シリカ<br>水溶性ケイ素miro</h3>
    <ul>
      <li>機能性、安全性エビデンスが充実<br>（ヒト臨床試験済、界面活性データ）</li>
      <li>アジア各国の認証取得原料</li>
      <li>シリカは鉱物由来、植物由来の<br>2種タイプから選択可能</li>
    </ul>
  </section>

  <div class="times">×</div>

  <section class="col-right">
    <h3>科学的に優れた<br>機能水</h3>
    <div class="compare">
      <figure><div class="swatch normal" role="img" aria-label="一般的な水の分子イメージ図"></div><figcaption>一般的な水</figcaption></figure>
      <figure><div class="swatch active" role="img" aria-label="生体機能水の微細分子イメージ図"></div><figcaption>生体機能水</figcaption></figure>
    </div>
    <p>微細分子が活性化<br>⇒浸透性が高い</p>
  </section>
</main>
</body>
</html>
```